Auto Mechanic business card

Need a general business card for GearFixer.
Name on card should be 'Roadside Wrench'
Tel # (869) 412 3097
Address is - Palm Lane, Basseterre, St. Kitts
Whatsapp and facebook symbols should be added
On back of card should include services offered
General Repairs
Brakes
Tune Ups
Suspensions
Oil Leaks
Dent repairs
Suspensions
Car Sales
Tyre Repairs
General service
Check Engine Light
Minor Electricals

Target Market(s)

General Population, University students

Industry/Entity Type

Auto Mechanic

Contact Information for Business Card

Roadside Wrench

Requirements
Must have
• 2 Sides

```html
<!DOCTYPE html>
<html lang="en">
<head>
<meta charset="utf-8">
<title>Roadside Wrench – Business Card</title>
<link rel="stylesheet" href="https://fonts.googleapis.com/css2?family=Signika:wght@600&family=Arimo:wght@400;700&family=Raleway:wght@400&display=swap">
<style>
  :root {
    --backdrop: #afafaf;
    --shadow: #8c8c8c;
    --sun: #ffcc00;
    --berry: #a3163d;
    --white: #ffffff;
    --steel: #5a8fc4;
    --steel-soft: #8cc4ee;
  }
  html, body {
    margin: 0;
    padding: 0;
    width: 1134px;
    height: 1200px;
    overflow: hidden;
    background: var(--backdrop);
  }
  .canvas {
    position: relative;
    width: 1134px;
    height: 1200px;
  }
  .card {
    position: absolute;
    left: 273px;
    width: 588px;
    height: 354px;
    box-shadow: 10px 8px 0 var(--shadow);
    overflow: hidden;
  }
  .card--front { top: 205px; background: var(--sun); }
  .card--back { top: 641px; background: var(--berry); }

  .brand-art {
    position: absolute;
    left: 125px;
    top: 33px;
    width: 347px;
    height: 150px;
    border-radius: 20px;
    background: linear-gradient(180deg, var(--steel-soft) 0%, var(--steel) 100%);
  }
  .brand-name {
    position: absolute;
    left: 0;
    right: 0;
    top: 186px;
    text-align: center;
    margin: 0;
    font-family: "Signika", sans-serif;
    font-weight: 600;
    font-size: 45px;
    line-height: 50px;
    letter-spacing: -0.5px;
    color: var(--berry);
  }
  .front-band {
    position: absolute;
    left: 0;
    right: 0;
    top: 257px;
    height: 97px;
  }
  .contact {
    position: absolute;
    left: 45px;
    top: 283px;
    font-family: "Arimo", sans-serif;
    font-size: 20px;
    line-height: 25px;
    color: var(--white);
  }
  .contact__phone { font-weight: 700; margin: 0; }
  .contact__address { font-weight: 400; margin: 0; }
  .social {
    position: absolute;
    left: 451px;
    top: 296px;
    display: flex;
    gap: 5px;
  }
  .social__dot {
    width: 34px;
    height: 34px;
    border-radius: 50%;
    background: var(--sun);
  }

  .services-title {
    position: absolute;
    left: 45px;
    top: 62px;
    margin: 0;
    font-family: "Signika", sans-serif;
    font-weight: 600;
    font-size: 40px;
    line-height: 50px;
    color: var(--white);
  }
  .services-title__accent { color: var(--sun); }
  .title-rule {
    position: absolute;
    left: 0;
    top: 110px;
  }
  .services-list {
    position: absolute;
    left: 45px;
    top: 138px;
    margin: 0;
    padding: 0;
    list-style: none;
    font-family: "Raleway", sans-serif;
    font-size: 19.5px;
    line-height: 24.2px;
    color: var(--white);
  }
  .back-band {
    position: absolute;
    left: 0;
    right: 0;
    top: 299px;
    height: 55px;
  }
</style>
</head>
<body>
<main class="canvas">

  <section class="card card--front" aria-label="Front of card">
    <div class="brand-art" role="img" aria-label="Illustration of mechanic tools, oil can and a red car with open bonnet"></div>
    <h1 class="brand-name">Roadside Wrench</h1>
    <svg class="front-band" width="588" height="97" viewBox="0 0 588 97" aria-hidden="true">
      <rect x="0" y="0" width="588" height="5" fill="var(--berry)"/>
      <rect x="0" y="5" width="588" height="4" fill="var(--sun)"/>
      <rect x="0" y="9" width="588" height="88" fill="var(--berry)"/>
    </svg>
    <div class="contact">
      <p class="contact__phone">Tel # (869) 412 3097</p>
      <p class="contact__address">Palm Lane, Basseterre, St. Kitts</p>
    </div>
    <div class="social" aria-label="Social channels">
      <span class="social__dot"></span>
      <span class="social__dot"></span>
    </div>
  </section>

  <section class="card card--back" aria-label="Back of card">
    <h2 class="services-title"><span class="services-title__accent">CAR</span>SERVICES</h2>
    <svg class="title-rule" width="370" height="12" viewBox="0 0 370 12" aria-hidden="true">
      <polygon points="0,0 368,0 356,12 0,12" fill="var(--sun)"/>
    </svg>
    <ul class="services-list">
      <li>General Repairs &nbsp;I Brakes &nbsp;I &nbsp;Tune Ups</li>
      <li>Suspensions &nbsp;I &nbsp;Oil Leaks &nbsp;I &nbsp;Dent repairs</li>
      <li>Suspensions &nbsp;I &nbsp;Car Sales &nbsp;I &nbsp;Tyre Repairs</li>
      <li>General service &nbsp;I &nbsp;Check Engine Light</li>
      <li>Minor Electricals</li>
    </ul>
    <svg class="back-band" width="588" height="55" viewBox="0 0 588 55" aria-hidden="true">
      <rect x="0" y="0" width="588" height="3" fill="var(--sun)"/>
      <rect x="0" y="3" width="588" height="3" fill="var(--berry)"/>
      <rect x="0" y="6" width="588" height="49" fill="var(--sun)"/>
    </svg>
  </section>

</main>
</body>
</html>
```